Silver Heron Paddle Club (Tennis Country Club)

Racquet and Tennis Country Club in Florida.
This web sight is needed for a Privet Tennis club located in Deerfield Beach city in Florida, USA.
We have 10 clay tennis courts and 2 hard tennis courts, small and cozy swimming pool and a clubhouse (see attached pictures) Attached pictures are for information only because we are under a reconstruction.
Updates

I haven't received any source files and web converted files neither!

Target Market(s)

Adult members, Kids members, Tennis players

Coding

Coded - Design and coding required

Number of Pages Required

3 page

Requirements
Must have
• Logo colors (see attached file)

```html
<!DOCTYPE html>
<html lang="en">
<head>
<meta charset="utf-8">
<title>Silver Heron Paddle Club</title>
<link href="https://fonts.googleapis.com/css2?family=Lato:wght@400;700&family=Raleway:wght@500;700;800&display=swap" rel="stylesheet">
<style>
:root{
  --green:#1d5e33;
  --green-dark:#123f22;
  --ink:#222;
  --charcoal:#3a3a3a;
  --muted:#555;
  --white:#fff;
  --light:#ececec;
  --footer:#e6e6e6;
}
*{margin:0;padding:0;box-sizing:border-box}
html,body{width:1200px;height:3495px;overflow:hidden}
body{font-family:"Lato",sans-serif;color:var(--ink);background:var(--white);position:relative}
.abs{position:absolute}

/* header */
.site-header{position:absolute;top:0;left:0;width:1200px;height:88px;background:var(--white);z-index:3}
.brand{position:absolute;left:113px;top:-20px;width:160px;height:165px;border-radius:50%;background:var(--white);z-index:4;display:flex;flex-direction:column;align-items:center;justify-content:flex-end;padding-bottom:38px}
.brand-mark{width:50px;height:50px;border:4px solid var(--green);border-radius:50%;margin-bottom:6px}
.brand-name{font-family:"Raleway",sans-serif;font-weight:700;font-size:22px;color:var(--charcoal);white-space:nowrap}
.main-nav{position:absolute;top:26px;left:457px;display:flex;font-family:"Raleway",sans-serif;font-weight:500;font-size:15px}
.main-nav a{color:var(--ink);text-decoration:none;height:37px;line-height:37px;position:absolute;white-space:nowrap}
.main-nav .active{background:var(--green);color:var(--white);width:79px;text-align:center;left:0}

/* hero */
.hero{top:88px;left:0;width:1200px;height:592px;background:linear-gradient(180deg,#0b0f0b 0%,#1a2a17 35%,#3f6a2b 70%,#6a9a3f 100%)}
.hero-title{left:123px;top:300px;font-family:"Raleway",sans-serif;font-weight:800;font-size:56px;color:var(--white)}
.hero-text{left:123px;top:388px;width:640px;font-family:"Raleway",sans-serif;font-weight:500;font-size:25px;line-height:34px;color:var(--white)}
.arrow-btn{width:40px;height:40px;border-radius:50%;background:var(--white);display:flex;align-items:center;justify-content:center}
.dots{display:flex;gap:8px}
.dots span{width:10px;height:10px;border-radius:50%;background:var(--white)}
.dots .on{background:var(--green)}

/* focus */
.eyebrow{top:775px;width:1200px;text-align:center;font-size:17px;color:var(--ink)}
.section-title{width:1200px;text-align:center;font-weight:700;font-size:30px;color:var(--ink)}
.focus-card{width:290px;height:290px}
.focus-body{position:absolute;left:24px;top:24px;width:242px;height:242px;border-radius:50%;background:#efefef;display:flex;flex-direction:column;align-items:center;padding-top:52px;text-align:center}
.focus-body h3{font-size:21px;font-weight:700;margin-top:10px;color:var(--ink)}
.focus-body p{font-size:12px;line-height:22px;color:var(--muted);width:190px;margin-top:6px}

/* gallery */
.gallery{top:1305px;left:0;width:1200px;height:822px;background:var(--light)}
.tile{position:absolute;display:flex;align-items:center;justify-content:center}
.tile-label{position:absolute;left:0;width:100%;height:52px;background:rgba(30,30,30,.72);color:var(--white);font-size:16px;display:flex;align-items:center;justify-content:center}

/* testimonials */
.testimonials{top:2127px;left:0;width:1200px;height:622px;background:linear-gradient(100deg,#1b2418 0%,#2a3a24 45%,#4c4f44 75%,#2c332a 100%)}
.light-text{color:var(--white);text-align:center;width:1200px}
.avatar{left:508px;top:2346px;width:140px;height:140px;border-radius:50%;background:#8a6a55;border:4px solid var(--white)}
.quote-badge{left:610px;top:2434px;width:54px;height:54px;border-radius:50%;background:var(--white);color:var(--green);font-family:"Raleway",sans-serif;font-weight:800;font-size:34px;text-align:center;line-height:62px}
.outline-arrow{width:30px;height:40px}

/* join */
.join{top:2749px;left:0;width:1200px;height:401px;background:radial-gradient(circle at 900px 300px,#3f8a4a 0,#1f6a33 30%,#145026 70%)}
.join-btn{left:536px;top:3017px;width:126px;height:42px;border:1.5px solid var(--white);color:var(--white);font-size:14px;display:flex;align-items:center;justify-content:center}

/* footer */
.site-footer{top:3150px;left:0;width:1200px;height:345px;background:var(--footer)}
.footer-heading{top:3208px;font-size:18px;font-weight:700;color:var(--ink)}
.blog-list{left:98px;top:3254px;list-style:none}
.blog-list li{font-size:12px;color:var(--muted);height:30px;padding-left:22px;position:relative}
.blog-list li::before{content:"";position:absolute;left:2px;top:4px;border-left:5px solid var(--charcoal);border-top:4px solid transparent;border-bottom:4px solid transparent}
.tweet{left:415px;width:310px;display:flex;gap:22px}
.tweet-icon{width:32px;height:32px;border-radius:4px;background:var(--charcoal);flex:none}
.tweet p{font-size:12.5px;line-height:20px;color:var(--muted)}
.tweet-rule{left:468px;top:3304px;width:244px;height:1px;background:#bbb}
.thumb{top:3274px;width:99px;height:95px}
.footer-rule{left:98px;top:3428px;width:1004px;height:1px;background:#9a9a9a}
.copyright{top:3452px;width:1200px;text-align:center;font-size:12px;color:var(--muted)}
</style>
</head>
<body>

<header class="site-header">
  <nav class="main-nav">
    <a class="active" href="#">Home</a>
    <a href="#" style="left:149px">About</a>
    <a href="#" style="left:254px">Events</a>
    <a href="#" style="left:379px">Membership</a>
    <a href="#" style="left:505px">Gallery</a>
    <a href="#" style="left:617px">Contact</a>
  </nav>
</header>
<div class="brand abs">
  <div class="brand-mark"></div>
  <div class="brand-name">Silver Heron</div>
</div>

<section class="hero abs" role="img" aria-label="Close-up of a tennis ball resting on a grass court line"></section>
<h1 class="hero-title abs">Silver Heron Tennis Club</h1>
<p class="hero-text abs">Perspiciatis unde omnis iste natus error sit voluptatem accusantium doloremque laudantium, totam rem</p>
<div class="arrow-btn abs" style="left:23px;top:378px"><svg width="20" height="20" viewBox="0 0 20 20"><path d="M17 10H4M10 4l-6 6 6 6" fill="none" stroke="#222" stroke-width="3"/></svg></div>
<div class="arrow-btn abs" style="left:1107px;top:378px"><svg width="20" height="20" viewBox="0 0 20 20"><path d="M3 10h13M10 4l6 6-6 6" fill="none" stroke="#222" stroke-width="3"/></svg></div>
<div class="dots abs" style="left:575px;top:636px"><span></span><span class="on"></span><span></span></div>

<p class="eyebrow abs">TENNIS CLUB</p>
<h2 class="section-title abs" style="top:810px">OUR FOCUS</h2>

<div class="focus-card abs" style="left:95px;top:899px">
  <svg class="abs" width="290" height="290" viewBox="0 0 290 290"><circle cx="145" cy="145" r="131" fill="none" stroke="var(--green)" stroke-width="18" stroke-dasharray="330 493" transform="rotate(-175 145 145)"/><circle cx="145" cy="145" r="131" fill="none" stroke="var(--charcoal)" stroke-width="18" stroke-dasharray="410 413" transform="rotate(8 145 145)"/></svg>
  <div class="focus-body"><svg width="70" height="70" viewBox="0 0 70 70"><circle cx="35" cy="33" r="14" fill="#222"/><path d="M14 20q-6 18 10 32M56 20q6 18-10 32" fill="none" stroke="#222" stroke-width="4"/><path d="M28 60h14" stroke="#222" stroke-width="4"/></svg><h3>Tournaments</h3><p>Excepteur sint occaecat cupidatat non proident, sunt in culpa</p></div>
</div>
<div class="focus-card abs" style="left:456px;top:899px">
  <svg class="abs" width="290" height="290" viewBox="0 0 290 290"><circle cx="145" cy="145" r="131" fill="none" stroke="var(--green)" stroke-width="18" stroke-dasharray="330 493" transform="rotate(-175 145 145)"/><circle cx="145" cy="145" r="131" fill="none" stroke="var(--charcoal)" stroke-width="18" stroke-dasharray="410 413" transform="rotate(8 145 145)"/></svg>
  <div class="focus-body"><svg width="70" height="70" viewBox="0 0 70 70"><ellipse cx="42" cy="26" rx="16" ry="14" transform="rotate(-40 42 26)" fill="none" stroke="#222" stroke-width="4"/><path d="M30 38L12 60" stroke="#222" stroke-width="6"/><circle cx="18" cy="20" r="6" fill="#222"/></svg><h3>Instruction</h3><p>Excepteur sint occaecat cupidatat non proident, sunt in culpa</p></div>
</div>
<div class="focus-card abs" style="left:817px;top:899px">
  <svg class="abs" width="290" height="290" viewBox="0 0 290 290"><circle cx="145" cy="145" r="131" fill="none" stroke="var(--green)" stroke-width="18" stroke-dasharray="330 493" transform="rotate(-175 145 145)"/><circle cx="145" cy="145" r="131" fill="none" stroke="var(--charcoal)" stroke-width="18" stroke-dasharray="410 413" transform="rotate(8 145 145)"/></svg>
  <div class="focus-body"><svg width="70" height="70" viewBox="0 0 70 70"><circle cx="32" cy="24" r="14" fill="none" stroke="#222" stroke-width="4"/><path d="M8 66q0-22 24-22t24 22" fill="none" stroke="#222" stroke-width="4"/><circle cx="54" cy="52" r="9" fill="var(--green)"/></svg><h3>Membership</h3><p>Excepteur sint occaecat cupidatat non proident, sunt in culpa</p></div>
</div>

<section class="gallery abs">
  <h2 class="section-title abs" style="top:72px">GALLERY</h2>
</section>
<div class="tile" role="img" aria-label="Rendering of the hard tennis courts beside the clubhouse" style="left:98px;top:1482px;width:282px;height:256px;background:linear-gradient(135deg,#d9d9d9,#8e8e8e)"><div class="tile-label">HARD TENNIS COURTS</div></div>
<div class="tile" role="img" aria-label="Swimming pool at night" style="left:408px;top:1482px;width:279px;height:256px;background:linear-gradient(160deg,#22303a,#1c4e6a)"><svg class="abs" style="top:88px" width="30" height="30" viewBox="0 0 30 30"><g fill="none" stroke="#fff" stroke-width="3"><rect x="3" y="3" width="14" height="9" rx="4.5" transform="rotate(45 10 7)"/><rect x="13" y="17" width="14" height="9" rx="4.5" transform="rotate(45 20 21)"/></g></svg><div class="tile-label" style="top:128px;background:rgba(20,30,40,.55)">SWIMMING POOL</div></div>
<div class="tile" role="img" aria-label="Clay tennis courts under a rainbow sky" style="left:711px;top:1482px;width:389px;height:540px;background:linear-gradient(180deg,#5a7fc0 0%,#8fb0dc 40%,#3f6a3c 70%,#244d6a 100%)"><div class="tile-label" style="top:246px">CLAY TENNIS COURTS</div></div>
<div class="tile" role="img" aria-label="Clubhouse terrace with wooden pergola" style="left:98px;top:1766px;width:282px;height:256px;background:linear-gradient(180deg,#9a5a35 0%,#6a6a6a 30%,#3a3a3a 100%)"><div class="tile-label" style="top:104px">CLUB HOUSE</div></div>
<div class="tile" role="img" aria-label="Clubhouse entrance at night" style="left:408px;top:1766px;width:279px;height:256px;background:linear-gradient(180deg,#151815,#2a3a2a)"><div class="tile-label" style="top:104px">CLUB HOUSE</div></div>

<section class="testimonials abs" role="img" aria-label="Woman playing tennis in the evening, darkened backdrop"></section>
<h2 class="section-title abs light-text" style="top:2208px">PLAYER TESTIMONIALS</h2>
<p class="abs light-text" style="top:2258px;font-size:17px">Excepteur sint occaecat cupidatat non proident, sunt in culpa qui officia deserunt</p>
<div class="avatar abs" role="img" aria-label="Portrait of club member"></div>
<div class="quote-badge abs">“</div>
<p class="abs light-text" style="top:2518px;font-size:17px">Commodo consequat</p>
<p class="abs light-text" style="top:2568px;font-size:13px;font-style:italic;line-height:28px">“Lorem ipsum dolor sit amet, consectetur adipiscing elit, sed do eiusmod tempor incididunt ut labore et dolore magna aliqua.<br>Ut enim ad minim veniam, quis nostrud exercitation ullamco laboris nisi ut aliquip ex ea commodo consequat”</p>
<div class="dots abs" style="left:575px;top:2651px"><span style="background:transparent;border:1.5px solid #fff"></span><span></span><span></span></div>
<svg class="outline-arrow abs" style="left:76px;top:2396px" viewBox="0 0 30 40"><path d="M22 4L8 20l14 16" fill="none" stroke="#fff" stroke-width="4"/></svg>
<svg class="outline-arrow abs" style="left:1096px;top:2396px" viewBox="0 0 30 40"><path d="M8 4l14 16L8 36" fill="none" stroke="#fff" stroke-width="4"/></svg>

<section class="join abs" role="img" aria-label="Green-toned tennis ball and racquet backdrop"></section>
<h2 class="section-title abs light-text" style="top:2831px">JOIN OUR CLUB</h2>
<p class="abs light-text" style="top:2877px;font-size:18px">Quis nostrud exercitation ullamco laboris nisi ut aliquip</p>
<p class="abs light-text" style="top:2927px;font-size:13.5px;line-height:29px">Excepteur sint occaecat cupidatat non proident, sunt in culpa qui officia deserunt mollit anim id est laborum<br>Duis aute irure dolor in reprehenderit in voluptate velit esse cillum dolore eu fugiat nulla pariatur.</p>
<a class="join-btn abs">Join Today</a>

<footer class="site-footer abs"></footer>
<h4 class="footer-heading abs" style="left:98px">Recent from the blog</h4>
<h4 class="footer-heading abs" style="left:415px">Tweets</h4>
<h4 class="footer-heading abs" style="left:774px">Latest Photos</h4>
<ul class="blog-list abs">
  <li>Nam libero tempore, cum soluta nobis est</li>
  <li>Nam libero tempore, cum soluta nobis est</li>
  <li>Nam libero tempore, cum soluta nobis est</li>
</ul>
<div class="tweet abs" style="top:3255px"><span class="tweet-icon"></span><p>Lorem ipsum dolor sit amet, consectetur adipiscing elit, sed do eiusmod tempor</p></div>
<div class="tweet-rule abs"></div>
<div class="tweet abs" style="top:3334px"><span class="tweet-icon"></span><p>Lorem ipsum dolor sit amet, consectetur adipiscing elit, sed do eiusmod tempor</p></div>
<div class="thumb abs" role="img" aria-label="Clubhouse rendering" style="left:774px;background:linear-gradient(135deg,#cfcfcf,#6f6f6f)"></div>
<div class="thumb abs" role="img" aria-label="Courts rendering" style="left:885px;background:linear-gradient(135deg,#dcdcdc,#7a7a7a)"></div>
<div class="thumb abs" role="img" aria-label="Clubhouse exterior rendering" style="left:1000px;width:100px;background:linear-gradient(135deg,#e4e4e4,#8a8a8a)"></div>
<div class="footer-rule abs"></div>
<p class="copyright abs">Copyright © 2018 Silver Heron. All rights reserved</p>

</body>
</html>
```